Trevor Outreach Group's Primary Marketing Brochure (Gate Fold Format)

We are looking for a main brochure design to communicate our company's primary mission, the need, where we meet the needs, how we meet the needs, and how the reader can get involved. We would like to see the color palette be similar to the colors of our company logo (attached). We would like to see a brochure design similar to a "gate fold" offering 22"x8.5" fully opened and 5.5"x8.5" when closed. Front panel, inside panels, full spread panel, and back panel. Required Text for each panel and usable picture suggestions are attached along with the company logo. The design should clean, contemporary, and emotionally compelling.

Target Market(s)

40-65 years old male and female, religious-minded

Industry/Entity Type

It Company

Font styles to use
Sans Serif

Requirements
Must have
• include text from attached WORD document.
• Clean, contemporary design
• Color in color palette of agency logo attached

```html
<!DOCTYPE html>
<html lang="en">
<head>
<meta charset="utf-8">
<title>Trevor Outreach Group – Gate Fold Brochure</title>
<link rel="stylesheet" href="https://fonts.googleapis.com/css2?family=PT+Sans:wght@400;700&display=swap">
<style>
  :root {
    --navy: #2b4a8e;
    --navy-deep: #223d78;
    --ink: #1e1e1e;
    --paper: rgba(255,255,255,0.86);
    --gold-dark: #a48a4f;
    --gold-light: #f4efe2;
    --globe: #5b5296;
    --photo-earth: #b79a78;
    --photo-green: #7f8a5a;
    --photo-warm: #c9b7a0;
  }
  * { box-sizing: border-box; margin: 0; padding: 0; }
  html, body { width: 1200px; height: 480px; overflow: hidden; background: #fff; }
  body { font-family: "PT Sans", Arial, sans-serif; color: var(--ink); }

  .brochure { position: relative; width: 1200px; height: 480px; overflow: hidden; }

  .top-band { position: absolute; left: 0; top: 0; width: 1200px; height: 77px; background: var(--navy); }
  .brand-box { position: absolute; left: 0; top: 14px; width: 308px; height: 63px; background: #fff;
    display: flex; align-items: center; padding-left: 46px; gap: 8px; }
  .brand-mark { width: 22px; height: 22px; border-radius: 50%; background: var(--navy); }
  .brand-name { font-size: 17px; font-weight: 700; color: var(--navy); }

  .contact { position: absolute; top: 34px; color: #fff; font-size: 9px; line-height: 13px;
    display: flex; align-items: center; gap: 6px; }
  .contact-address { left: 351px; }
  .contact-phone { left: 740px; }
  .phone-icon { width: 13px; height: 13px; }
  .accredit-badge { position: absolute; left: 1068px; top: 17px; width: 42px; height: 42px; border-radius: 50%;
    background: #fff; border: 3px solid var(--navy-deep); }

  .photo { position: absolute; top: 77px; height: 361px; }
  .photo-left { left: 0; width: 308px;
    background: linear-gradient(180deg, var(--photo-green) 0%, var(--photo-earth) 40%, #a9855f 100%); }
  .photo-right { left: 892px; width: 308px;
    background: linear-gradient(160deg, var(--photo-warm) 0%, #a89278 55%, #8c7358 100%); }

  .gold-fade { position: absolute; top: 77px; height: 361px; width: 84px; }
  .gold-fade.left { left: 308px; background: linear-gradient(90deg, var(--gold-dark), var(--gold-light)); }
  .gold-fade.right { left: 808px; background: linear-gradient(90deg, var(--gold-light), var(--gold-dark)); }
  .center-panel { position: absolute; left: 392px; top: 77px; width: 416px; height: 361px; background: #fff; }
  .globe { position: absolute; left: 428px; top: 84px; width: 344px; height: 344px; border-radius: 50%;
    background: var(--globe); border: 10px solid var(--globe); box-shadow: inset 0 0 0 8px #fff; }

  .text-card { position: absolute; top: 92px; width: 262px; height: 330px; background: var(--paper);
    padding: 18px 13px 12px 13px; font-size: 8.5px; line-height: 10.4px; }
  .text-card.left { left: 28px; }
  .text-card.right { left: 908px; padding-top: 22px; }
  .text-card h2 { font-size: 10px; line-height: 13px; font-weight: 400; margin-bottom: 22px; }
  .text-card p { font-weight: 700; margin-bottom: 9px; }
  .text-card p:last-child { margin-bottom: 0; }
  .text-card .vision { margin-bottom: 18px; }
  .text-card .beliefs-title { margin-bottom: 9px; }
  .text-card.right p { margin-bottom: 10px; }
  .text-card.right p:last-child { margin-bottom: 0; }

  .bottom-band { position: absolute; left: 0; top: 438px; width: 1200px; height: 42px; background: var(--navy); }
</style>
</head>
<body>
<div class="brochure">
  <header class="top-band">
    <div class="brand-box">
      <span class="brand-mark"></span>
      <span class="brand-name">Trevor Outreach Group</span>
    </div>
    <div class="contact contact-address">410 Ridgeview Ave. Brookfield, TN. 37000-0142</div>
    <div class="contact contact-phone">
      <svg class="phone-icon" viewBox="0 0 16 16"><circle cx="8" cy="8" r="7" fill="none" stroke="#fff" stroke-width="1"/><path d="M5.5 4.5l1.5 0 .6 1.8-1 .7a5 5 0 0 0 2.4 2.4l.7-1 1.8.6v1.5c0 .5-.5.9-1 .8A6.5 6.5 0 0 1 4.7 5.5c-.1-.5.3-1 .8-1z" fill="#fff"/></svg>
      800-555-0142
    </div>
    <div class="accredit-badge"></div>
  </header>

  <div class="photo photo-left" role="img" aria-label="Photo of a dirt road through a village with people walking"></div>
  <div class="gold-fade left"></div>
  <div class="center-panel"></div>
  <div class="globe" role="img" aria-label="Purple globe illustration showing the Americas, Europe and Africa"></div>
  <div class="gold-fade right"></div>
  <div class="photo photo-right" role="img" aria-label="Photo of a child being cared for"></div>

  <section class="text-card left">
    <h2>•Vision of Trevor Outreach Group</h2>
    <p class="vision">o&nbsp; Our vision is ever more communities all around the world radically transformed by the love of the Gospel...communities with reproducing, multiplying, Christ-centered national leaders who are part of thriving, engaged local churches growing committed disciples of Jesus, boldly proclaiming the Good News, compassionately caring for spiritual and physical needs, and advancing the Kingdom in all aspects of society.</p>
    <p class="beliefs-title">We believe:</p>
    <p>• in the Scriptures of the Old and New Testament as inspired by God and inerrant in the original writings and that they are the supreme and final authority in faith and life.</p>
    <p>• in one God, eternally existing in three persons: Father, Son, and Holy Spirit.</p>
    <p>• that Jesus Christ was begotten by the Holy Spirit and born of the virgin Mary and is true God and true man.</p>
    <p>• that man was created in the image of God, that he sinned and thereby incurred not only physical death but also that spiritual death which is separation from God, and that all human beings are born with a sinful nature.</p>
  </section>

  <section class="text-card right">
    <p>• that the Lord Jesus Christ died for our sins, according to the Scriptures, as a representative and substitutionary sacrifice, and that all who believe in Him are justified on the ground of His shed blood.</p>
    <p>• in the bodily resurrection of our crucified Lord, His ascension into heaven and His presence there for us as High Priest and Advocate.</p>
    <p>• in that “blessed hope”—the personal and victorious return of our Lord and Savior, Jesus Christ.</p>
    <p>• that all who receive by repentance and faith the Lord Jesus Christ are born again of the Holy Spirit, and become children of God.</p>
    <p>• in the bodily resurrection of the just and unjust, the everlasting blessedness of the saved and the everlasting punishment of the lost.</p>
    <p>• that, according to the specific teachings of the entire Bible, which is the written Word of God, God created man and women as unique biological persons made to complete each other, and that human sexuality in God’s plan is to be expressed only within the context of monogamous marriage between a genetic male and a genetic female, and that such marriage is the foundation of the family and the basic structure of human society.</p>
  </section>

  <footer class="bottom-band"></footer>
</div>
</body>
</html>
```